Business Card Design Project

We are looking for a new business card design for a Drilling company in WA, Australia.

We are in between offices, however require a design in the meantime due to some upcoming events with our basic information.

The Logo for our company is Blue and Grey and would like this colour scheme throughout.

We are quite a new company so would like a memorable design that stands out and communicates a strong commitment to safety, quality of work and performance.

The company name is Ironbark Boring Group (IBG)

The details to be included are as follows:

Gavin Thorley
Managing Director
m.0481639207
e.gavin@ibgpty.com.au

Martin Thorley
Director
m.0419852637
e.martin@ibgpty.com.au

Industry/Entity Type

Events

Requirements
Must have
• Under the Logo, we would like 'Western Australia'

```html
<!DOCTYPE html>
<html lang="en">
<head>
<meta charset="utf-8">
<title>Ironbark Boring Group – Business Cards</title>
<link rel="stylesheet" href="https://fonts.googleapis.com/css2?family=Source+Sans+3:wght@400;600;700&display=swap">
<style>
  :root {
    --brand-blue: #0b3f87;
    --brand-grey: #6f6f6f;
    --text-grey: #555555;
    --card-white: #ffffff;
    --stage: #eceae6;
  }
  * { box-sizing: border-box; margin: 0; padding: 0; }
  html, body {
    width: 1200px; height: 444px; overflow: hidden;
    background: var(--stage);
    font-family: "Source Sans 3", "Helvetica Neue", Arial, sans-serif;
  }
  .canvas { position: relative; width: 1200px; height: 444px; }

  .card {
    position: absolute; top: 72px;
    width: 526px; height: 300px;
    border-radius: 14px;
    box-shadow: 0 3px 8px rgba(0,0,0,0.18);
  }
  .card--front { left: 60px; background: var(--card-white); }
  .card--back  { left: 614px; background: var(--brand-blue); }

  .brand { position: absolute; text-align: right; }
  .brand__name { font-weight: 700; line-height: 1; white-space: nowrap; }
  .brand__region { font-weight: 700; letter-spacing: 0.06em; margin-top: 6px; }

  .card--front .brand { left: 140px; top: 84px; width: 250px; }
  .card--front .brand__name { font-size: 24px; color: var(--brand-blue); text-align: center; }
  .card--front .brand__region { font-size: 8px; color: var(--brand-blue); }

  .card--back .brand { left: 108px; top: 112px; width: 310px; }
  .card--back .brand__name { font-size: 30px; color: var(--card-white); text-align: center; }
  .card--back .brand__region { font-size: 10px; color: var(--card-white); }

  .contact { position: absolute; top: 184px; }
  .contact--director { right: 258px; text-align: right; }
  .contact--managing { left: 304px; text-align: left; }
  .contact__name { font-size: 17px; font-weight: 700; color: var(--brand-blue); line-height: 1.2; }
  .contact__role { font-size: 13px; color: var(--text-grey); line-height: 1.2; }
  .contact__lines { margin-top: 14px; list-style: none; }
  .contact__line {
    display: flex; align-items: center; gap: 7px;
    font-size: 13px; color: var(--text-grey); line-height: 20px;
  }
  .contact--director .contact__line { justify-content: flex-end; }
  .icon { width: 10px; height: 10px; flex: none; fill: var(--brand-blue); }
</style>
</head>
<body>
<main class="canvas">
  <section class="card card--front">
    <div class="brand">
      <p class="brand__name">Ironbark Boring Group</p>
      <p class="brand__region">Western Australia</p>
    </div>

    <div class="contact contact--director">
      <p class="contact__name">Martin Thorley</p>
      <p class="contact__role">Director</p>
      <ul class="contact__lines">
        <li class="contact__line">041-985-2637
          <svg class="icon" viewBox="0 0 10 10" aria-hidden="true"><rect x="2" y="0" width="6" height="10" rx="1"/><rect x="3" y="1.5" width="4" height="4" fill="#fff"/></svg>
        </li>
        <li class="contact__line">e.martin@ibgpty.com.au
          <svg class="icon" viewBox="0 0 10 10" aria-hidden="true"><rect x="0" y="2" width="10" height="7"/><path d="M0 2 L5 6 L10 2" fill="none" stroke="#fff" stroke-width="1"/></svg>
        </li>
      </ul>
    </div>

    <div class="contact contact--managing">
      <p class="contact__name">Gavin Thorley</p>
      <p class="contact__role">Managing Director</p>
      <ul class="contact__lines">
        <li class="contact__line">
          <svg class="icon" viewBox="0 0 10 10" aria-hidden="true"><rect x="2" y="0" width="6" height="10" rx="1"/><rect x="3" y="1.5" width="4" height="4" fill="#fff"/></svg>048-163-9207
        </li>
        <li class="contact__line">
          <svg class="icon" viewBox="0 0 10 10" aria-hidden="true"><rect x="0" y="2" width="10" height="7"/><path d="M0 2 L5 6 L10 2" fill="none" stroke="#fff" stroke-width="1"/></svg>gavin@ibgpty.com.au
        </li>
      </ul>
    </div>
  </section>

  <section class="card card--back">
    <div class="brand">
      <p class="brand__name">Ironbark Boring Group</p>
      <p class="brand__region">Western Australia</p>
    </div>
  </section>
</main>
</body>
</html>
```